Promotion flyer for chair massage

What i need is a design for a 2 page flyer. Im gonna give it to a company so their employe can learn about the service and how they can take an appointements with us. The text is in french because i work in a french company.
On first page(FRONT PAGE) i want the name of the company VITALOMAX inc.
and bellow : Massothérapie sur chaise en entreprise
On the second page(INSIDE) i want the benefits :
Les Bienfaits
- DIMINUTION DU STRESS
- AMÉLIORATION DU BIEN-ÊTRE PHYSIQUE ET PSYCHOLOGIQUE
- AUGMENTATION DE L’ÉNERGIE
- SOULAGE LES MAUX DE DOS ET DE TÊTE
- AMÉLIORE VOTRE QUALITÉ DE SOMMEIL
On the third page (INSIDE) I want the steps to take an appointment :
Obtenez votre massage en quelques clics
1. Allez sur https://www.prenezplace-exemple.com/vitalomax
2. Choisir le nombre de minute désirer (10-15-20-30)
3. Choisir votre thérapeute
4. Choisir votre emplacement (lieu de travail)
5. Choisir votre plage horaire
6. Remplir votre fiche (Prénom-Nom-Email-#téléphone)
7. Aussi simple que ça !! À bientôt !
On the final page i want the text so they can contact me :
CONTACTEZ-NOUS
Mail : Info@vitalomax-exemple.ca
Tél. 438-555-0172
Site web : Vitalomax-exemple.ca
If you can respect the same kind of design that i already did in the past i would love it :)
Target Market(s)
Bank employee
Industry/Entity Type
Massage Therapy

```html
<!DOCTYPE html>
<html lang="fr">
<head>
<meta charset="utf-8">
<title>VITALOMAX inc. – Dépliant massothérapie sur chaise</title>
<link href="https://fonts.googleapis.com/css2?family=Barlow+Condensed:wght@400;700&family=Lato:wght@400;700&display=swap" rel="stylesheet">
<style>
  :root {
    --backdrop: #3a3a3c;
    --paper: #ffffff;
    --ink: #262626;
    --muted: #555555;
    --brand-blue: #1c5aa6;
    --panel-blue: #2a5b98;
    --photo-deep: #1f4a8a;
    --photo-mid: #4a72b4;
    --photo-light: #9db6de;
    --stripe: #c9d6ea;
  }
  * { margin: 0; padding: 0; box-sizing: border-box; }
  html, body { width: 1200px; height: 1200px; overflow: hidden; background: var(--backdrop); }
  .stage { position: relative; width: 1200px; height: 1200px; }

  .spread { position: absolute; left: 54px; width: 1092px; height: 386px; background: var(--paper); display: flex; }
  .spread--outside { top: 198px; }
  .spread--inside { top: 616px; }
  .page { position: relative; width: 546px; height: 100%; overflow: hidden; }

  .brand { position: absolute; display: flex; flex-direction: column; align-items: center; }
  .brand__name { font-family: "Lato", sans-serif; font-weight: 700; color: var(--brand-blue); line-height: 1; letter-spacing: 0.3px; }
  .brand__tag { font-family: "Lato", sans-serif; font-weight: 400; color: var(--muted); letter-spacing: 1px; text-transform: uppercase; margin-top: 6px; }

  .brand--large { left: 0; right: 0; top: 24px; }
  .brand--large .brand__name { font-size: 26px; }
  .brand--large .brand__tag { font-size: 9px; }

  .brand--small { left: 22px; top: 24px; align-items: flex-start; }
  .brand--small .brand__name { font-size: 17px; }
  .brand--small .brand__tag { font-size: 6px; margin-top: 4px; }

  .photo { position: absolute; left: 0; width: 100%; }
  .photo--office { top: 75px; height: 217px; background: linear-gradient(160deg, var(--photo-light) 0%, var(--photo-mid) 45%, var(--photo-deep) 100%); }
  .photo--closeup { top: 75px; height: 267px; background: radial-gradient(ellipse at 70% 40%, var(--photo-light) 0%, var(--photo-mid) 45%, var(--photo-deep) 100%); }

  .stripes { position: absolute; left: 0; top: 292px; }
  .stripes span { position: absolute; left: 0; background: var(--stripe); opacity: 0.8; }

  .contact { position: absolute; left: 348px; top: 314px; font-family: "Lato", sans-serif; font-size: 11.5px; line-height: 14px; color: var(--ink); }
  .contact__title { color: var(--brand-blue); font-weight: 700; }

  .cover-title { position: absolute; left: 0; right: 0; top: 349px; text-align: center; font-family: "Barlow Condensed", sans-serif; font-weight: 700; font-size: 20px; color: var(--brand-blue); letter-spacing: 0.2px; }

  .panel { position: absolute; left: 0; top: 75px; width: 100%; height: 267px; background: linear-gradient(120deg, #3a68a5 0%, var(--panel-blue) 55%, #23528f 100%); color: #fff; font-family: "Lato", sans-serif; }

  .benefits { position: absolute; left: 42px; top: 79px; }
  .benefits__title { font-weight: 700; font-size: 23px; line-height: 26px; margin-bottom: 2px; }
  .benefits__list { list-style: none; font-size: 12.5px; line-height: 15.6px; font-weight: 700; text-transform: uppercase; }
  .benefits__list li { position: relative; padding-left: 17px; }
  .benefits__list li::before { content: ""; position: absolute; left: 2px; top: 6px; width: 4px; height: 4px; border-radius: 50%; background: #fff; }

  .steps { position: absolute; left: 34px; top: 45px; }
  .steps__title { font-weight: 700; font-size: 21px; line-height: 24px; margin-bottom: 5px; }
  .steps__list { list-style: none; font-size: 12.5px; line-height: 15.6px; font-weight: 700; }

  .footer-url { position: absolute; right: 45px; top: 356px; font-family: "Lato", sans-serif; font-weight: 700; font-size: 12.5px; color: var(--brand-blue); }
</style>
</head>
<body>
<main class="stage">

  <section class="spread spread--outside">
    <article class="page page--back">
      <header class="brand brand--large">
        <span class="brand__name">VITALOMAX inc.</span>
        <span class="brand__tag">Massothérapie en entreprise</span>
      </header>
      <div class="photo photo--office" role="img" aria-label="Photo en bureau : une thérapeute masse une employée assise sur une chaise de massage, un collègue travaille sur un canapé"></div>
      <div class="stripes" aria-hidden="true">
        <span style="top:0;width:300px;height:12px;"></span>
        <span style="top:8px;width:230px;height:14px;"></span>
        <span style="top:22px;width:140px;height:12px;"></span>
        <span style="top:34px;width:195px;height:14px;"></span>
        <span style="top:48px;width:66px;height:14px;"></span>
      </div>
      <div class="contact">
        <p class="contact__title">CONTACTEZ-NOUS</p>
        <p>Mail : Info@vitalomax-exemple.ca</p>
        <p>Tél. 438-555-0172</p>
        <p>Site web : Vitalomax-exemple.ca</p>
      </div>
    </article>
    <article class="page page--front">
      <header class="brand brand--large">
        <span class="brand__name">VITALOMAX inc.</span>
        <span class="brand__tag">Massothérapie en entreprise</span>
      </header>
      <div class="photo photo--closeup" role="img" aria-label="Gros plan d'une main massant l'épaule d'une personne"></div>
      <h1 class="cover-title">MASSOTHÉRAPIE SUR CHAISE EN ENTREPRISE</h1>
    </article>
  </section>

  <section class="spread spread--inside">
    <article class="page page--benefits">
      <header class="brand brand--small">
        <span class="brand__name">VITALOMAX inc.</span>
        <span class="brand__tag">Massothérapie en entreprise</span>
      </header>
      <div class="panel" role="img" aria-label="Photo estompée d'un massothérapeute massant l'épaule d'une cliente">
        <div class="benefits">
          <h2 class="benefits__title">LES BIENFAITS</h2>
          <ul class="benefits__list">
            <li>Diminution du stress</li>
            <li>Amélioration du bien-être physique et psychologique</li>
            <li>Augmentation de l’énergie</li>
            <li>Soulage les maux de dos et de tête</li>
            <li>Améliore votre qualité de sommeil</li>
          </ul>
        </div>
      </div>
      <p class="footer-url">Vitalomax-exemple.ca</p>
    </article>
    <article class="page page--steps">
      <header class="brand brand--small">
        <span class="brand__name">VITALOMAX inc.</span>
        <span class="brand__tag">Massothérapie en entreprise</span>
      </header>
      <div class="panel" role="img" aria-label="Photo estompée d'une thérapeute massant une personne assise sur une chaise de massage">
        <div class="steps">
          <h2 class="steps__title">Obtenez votre massage en quelques clics</h2>
          <ol class="steps__list">
            <li>1. Allez sur https://www.prenezplace-exemple.com/vitalomax</li>
            <li>2. Choisir le nombre de minute désirer (10-15-20-30)</li>
            <li>3. Choisir votre thérapeute</li>
            <li>4. Choisir votre emplacement (lieu de travail)</li>
            <li>5. Choisir votre plage horaire</li>
            <li>6. Remplir votre fiche (Prénom-Nom-Email-#téléphone)</li>
            <li>7. Aussi simple que ça !! À bientôt !</li>
          </ol>
        </div>
      </div>
      <p class="footer-url">Vitalomax-exemple.ca</p>
    </article>
  </section>

</main>
</body>
</html>
```